BY MELVORE EXECUTIVE SERVICE BUSINESS CARDS. FAST

Need business card layout with round logo vs square logo

I have attached a mock up of the business card layout both front and back. I would like to change the square logo to the round logo. And change concierge services on the front of card to guest services. The two yellow highlight circles need to be changed. 1. Please make 1 flower all yellow 2. Please insert unique (use script font) between chief and experience. Use an up sweeping arrow and change to the teal color

Target Market(s)

Transportation

Industry/Entity Type

Transportation

Contact Information for Business Card

Logo large on one side and main business line such as Taxi or executive car service or Melvore Guest Services

Font styles to use
Decorative
Script
Other font styles liked:
• See logo especially the A In the logo

Colors
FFF300
FFF600
FEFA6F
FFFEC7
FFFEE8
FFC000
F8CF3A
FAE287
FDF2CF
FEFAEE

Requirements
Must have
• Logo Cool clean sophisticated design. Phone number list of services.
Nice to have
• Love the black with teal design but instead of vertical, please run line horizontal with a yellow flower splash/dot like the design
Should not have
• Childish animation.

```html
<!DOCTYPE html>
<html lang="en">
<head>
<meta charset="utf-8">
<title>Melvore Guest Services – Business Cards</title>
<link rel="stylesheet" href="https://fonts.googleapis.com/css2?family=Cinzel:wght@500&family=Open+Sans:wght@700&family=Anton&family=Allura&display=swap">
<style>
  :root {
    --stage: #1d1d1f;
    --card-black: #121113;
    --card-black-soft: #1c1b1d;
    --pattern-dark: #141416;
    --pattern-mid: #232326;
    --pattern-light: #34343a;
    --gold: #e2b43c;
    --gold-light: #f8cf3a;
    --gold-deep: #a9802c;
    --gold-pale: #e6d39c;
    --title-ink: #050505;
  }
  * { margin: 0; padding: 0; box-sizing: border-box; }
  html, body {
    width: 1200px;
    height: 874px;
    overflow: hidden;
    background: var(--stage);
  }
  .canvas {
    position: relative;
    width: 1200px;
    height: 874px;
    background: var(--stage);
  }
  .card {
    position: absolute;
    left: 280px;
    width: 640px;
    height: 366px;
    border-radius: 22px;
    overflow: hidden;
    box-shadow: 0 18px 40px rgba(0, 0, 0, 0.55);
  }
  .card--front { top: 40px; background: var(--pattern-dark); }
  .card--back {
    top: 460px;
    background: linear-gradient(110deg, var(--card-black) 0%, var(--card-black-soft) 45%, #2a292c 55%, var(--card-black) 75%);
  }

  .rose-pattern {
    position: absolute;
    inset: 0;
    background:
      radial-gradient(ellipse 60% 70% at 25% 30%, var(--pattern-light) 0%, transparent 70%),
      radial-gradient(ellipse 55% 60% at 80% 75%, var(--pattern-mid) 0%, transparent 70%),
      linear-gradient(135deg, var(--pattern-mid) 0%, var(--pattern-dark) 55%, #0e0e10 100%);
  }

  .brand-mark {
    position: absolute;
    left: 44px;
    top: 140px;
    width: 108px;
    height: 108px;
    border-radius: 50%;
    background: linear-gradient(160deg, var(--gold-deep) 0%, var(--gold-pale) 48%, var(--gold-deep) 100%);
    box-shadow: 0 4px 10px rgba(0, 0, 0, 0.6);
  }
  .brand-name {
    position: absolute;
    right: 38px;
    top: 226px;
    font-family: "Cinzel", serif;
    font-weight: 500;
    font-size: 33px;
    letter-spacing: 0.5px;
    white-space: nowrap;
    color: var(--gold);
  }
  .brand-phone {
    position: absolute;
    right: 38px;
    top: 274px;
    font-family: "Open Sans", sans-serif;
    font-weight: 700;
    font-size: 46px;
    letter-spacing: 2px;
    white-space: nowrap;
    color: var(--gold-light);
  }

  .role-title {
    position: absolute;
    left: 0;
    right: 0;
    top: 62px;
    text-align: center;
    font-family: "Anton", sans-serif;
    font-size: 150px;
    line-height: 1;
    letter-spacing: 4px;
    color: var(--title-ink);
  }
  .signature-swash {
    position: absolute;
    inset: 0;
  }
  .person-name {
    position: absolute;
    left: 40px;
    right: 0;
    top: 128px;
    text-align: center;
    font-family: "Allura", cursive;
    font-size: 110px;
    line-height: 1;
    color: var(--gold);
  }
</style>
</head>
<body>
<main class="canvas">
  <section class="card card--front">
    <div class="rose-pattern" role="img" aria-label="Tonal repeating rose pattern in glossy black"></div>
    <div class="brand-mark"></div>
    <p class="brand-name">Melvore Guest Services</p>
    <p class="brand-phone">555-014-2736</p>
  </section>

  <section class="card card--back">
    <p class="role-title">CONCIERGE</p>
    <svg class="signature-swash" width="640" height="366" viewBox="0 0 640 366" aria-hidden="true">
      <path d="M170 226 C 300 214, 440 232, 570 292" fill="none" stroke="var(--gold)" stroke-width="2"/>
    </svg>
    <p class="person-name">Marisol</p>
  </section>
</main>
</body>
</html>
```